Create a business Card for a Women Owned Business Body Positive Company. The winner we hope to work with on other projects coming up for grand opening for flyers, postcards, email marketing, facebook page, stationary, labels, tshirt design....
We would like if possible in the background of the card a infinity symbol or crown if it fits into the design if not it's ok. But I am open to all suggestions we had alot problems with the our new logo being created this time sad to say :(

Our colors are Royal Purple, Grey, Black Thank you in advance for your talent, you hard work and your submissions!
Delia and Harriet :)

my Logo is lantern meadow boutique which is purple and has a heart and infinity sign in it and my colors are purple silver and black only of another card i had done nothing else. My logo is LANTERN MEADOW BOUTIQUE LOGO

Industry/Entity Type

Retail

Contact Information for Business Card

website: www.lantrnmeadowboutiques.example email: sales@lanternmeadowboutique.example
Delia Rookwell & Harriet Quinlan Owners

Font styles to use
Script

Colors
b768aa

Requirements
Must have
• COLORS ARE PURPLE BLACK AND GREY
Nice to have
• INFINITY SIGNING IN THE BACKGROUND

```html
<!DOCTYPE html>
<html lang="en">
<head>
<meta charset="utf-8">
<title>Lantern Meadow Boutique – Business Card</title>
<link href="https://fonts.googleapis.com/css2?family=Cinzel:wght@400;500&family=Crimson+Text:wght@400;700&display=swap" rel="stylesheet">
<style>
  :root {
    --backdrop: #d9d6d2;
    --card-light: #f4f4f3;
    --card-dark: #221f21;
    --royal-purple: #6c3b98;
    --ink: #1d1b1c;
  }
  * { margin: 0; padding: 0; box-sizing: border-box; }
  html, body { width: 1200px; height: 960px; overflow: hidden; }
  body { background: var(--backdrop); position: relative; }

  .card {
    position: absolute;
    width: 600px;
    height: 343px;
    border-radius: 20px;
  }
  .card-front { left: 314px; top: 113px; background: var(--card-light); }
  .card-back  { left: 311px; top: 472px; background: var(--card-dark); }

  .front-frame {
    position: absolute;
    inset: 12px;
    border: 3px solid var(--royal-purple);
    border-radius: 18px;
  }

  .owner-names {
    position: absolute;
    top: 55px; left: 0; right: 0;
    text-align: center;
    font-family: "Cinzel", serif;
    font-weight: 500;
    color: var(--royal-purple);
    font-size: 23px;
    line-height: 27px;
  }
  .owner-role {
    position: absolute;
    top: 108px; left: 0; right: 0;
    text-align: center;
    font-family: "Cinzel", serif;
    font-weight: 500;
    font-size: 16px;
    letter-spacing: 1px;
    color: var(--ink);
  }
  .contact-list {
    position: absolute;
    top: 154px; left: 0; right: 0;
    text-align: center;
    font-family: "Crimson Text", serif;
    font-size: 17px;
    line-height: 20px;
    color: var(--ink);
    list-style: none;
  }
  .contact-label { color: var(--royal-purple); font-weight: 700; }

  .flourish-area {
    position: absolute;
    left: 149px; top: 229px;
    width: 304px; height: 114px;
  }

  .brand-name {
    position: absolute;
    left: 0; right: 0;
    top: 170px;
    text-align: center;
    font-family: "Cinzel", serif;
    font-weight: 400;
    color: var(--royal-purple);
  }
  .brand-name .brand-main { display: block; font-size: 34px; line-height: 38px; }
  .brand-name .brand-sub  { display: block; font-size: 15px; letter-spacing: 6px; margin-top: 4px; }
</style>
</head>
<body>

  <section class="card card-front" aria-label="Business card front">
    <div class="front-frame"></div>
    <h1 class="owner-names">Delia Rookwell<br>Harriet Quinlan</h1>
    <p class="owner-role">owners</p>
    <ul class="contact-list">
      <li><span class="contact-label">Email:</span> sales@lanternmeadowboutique.example</li>
      <li><span class="contact-label">Web:</span> lantrnmeadowboutiques.example</li>
    </ul>
    <svg class="flourish-area" viewBox="0 0 304 114" role="img" aria-label="Purple scrollwork flourish ornament along the bottom border">
      <defs>
        <radialGradient id="flourishTone" cx="50%" cy="70%" r="60%">
          <stop offset="0" stop-color="#6c3b98" stop-opacity="0.45"/>
          <stop offset="1" stop-color="#6c3b98" stop-opacity="0.12"/>
        </radialGradient>
      </defs>
      <rect x="0" y="20" width="304" height="94" rx="40" fill="url(#flourishTone)"/>
    </svg>
  </section>

  <section class="card card-back" aria-label="Business card back">
    <p class="brand-name">
      <span class="brand-main">LANTERN MEADOW</span>
      <span class="brand-sub">BOUTIQUE</span>
    </p>
  </section>

</body>
</html>
```